Valdet Company needs a Business Card Design

We just opened our business recently and we need a business card design. Our basic product are clothes and accessories. We would like to see designs that use bright colors like pink, light blue and purple. In addition to that kindly include also our address in the business card which our main office is located in Los Angeles, California.
The final design should communicate that we have affordable price yet high quality brand.

Target Market(s)

young and middle age women

Industry/Entity Type

Business

Contact Information for Business Card

Valdet Apparel and Accessories 3847 North Pelham St. Los Angeles California
Tel: 424-639-8852

Logo Text

Valdet's Apparel and Accessories

Font styles to use
Serif

Requirements
Must have
• there should be a graphic of a sexy lady wearing an elegant dress at the upper left corner of the business card.

```html
<!DOCTYPE html>
<html lang="en">
<head>
<meta charset="utf-8">
<title>Valdet Apparel and Accessories – Business Card</title>
<link rel="stylesheet" href="https://fonts.googleapis.com/css2?family=Open+Sans:wght@400;600&display=swap">
<style>
  :root {
    --brand-red: #e0212e;
    --ink: #1c1c1c;
    --ink-soft: #4a4a4a;
    --card: #ffffff;
    --backdrop: #e9e7e4;
    --ghost-red: #f3d9d6;
    --ghost-grey: #dcdcdc;
    --figure-tone: #f6dede;
  }
  * { margin: 0; padding: 0; box-sizing: border-box; }
  html, body {
    width: 1200px; height: 818px; overflow: hidden;
    background: var(--backdrop);
    font-family: "Open Sans", Arial, sans-serif;
  }
  .stage {
    position: relative; width: 1200px; height: 818px;
    display: flex; align-items: center; justify-content: center; gap: 40px;
  }
  .card {
    position: relative; width: 540px; height: 309px;
    background: var(--card);
    box-shadow: 0 6px 18px rgba(0,0,0,0.12);
    overflow: hidden;
  }
  /* Front */
  .brand-mark {
    position: absolute; left: 34px; top: 40px;
    width: 82px; height: 82px;
    border: 2px solid var(--brand-red);
    padding: 6px;
  }
  .brand-mark .figure-area {
    width: 100%; height: 100%;
    background: linear-gradient(180deg, #ffffff 0%, var(--figure-tone) 100%);
  }
  .brand-name {
    position: absolute; left: 134px; top: 18px;
    font-size: 74px; font-weight: 400; line-height: 1;
    color: var(--brand-red); letter-spacing: -1px;
  }
  .brand-tagline {
    position: absolute; left: 140px; top: 100px;
    font-size: 20px; color: var(--ink-soft); letter-spacing: 0.2px;
  }
  .person-name {
    position: absolute; left: 38px; top: 150px;
    font-size: 24px; font-weight: 600; color: var(--brand-red);
  }
  .person-title {
    position: absolute; left: 40px; top: 182px;
    font-size: 15px; color: var(--ink-soft);
  }
  .contact {
    position: absolute; left: 40px; top: 218px;
    font-size: 16px; line-height: 1.35; color: var(--ink);
  }
  .contact .phone-row { display: flex; align-items: center; gap: 8px; }
  .contact .phone-icon { width: 18px; height: 18px; flex: none; }
  .contact .address { padding-left: 26px; }
  /* Back */
  .ghost-name {
    position: absolute; right: 22px; top: 70px;
    font-size: 150px; line-height: 1; color: var(--ghost-red);
    letter-spacing: -2px;
  }
  .ghost-tagline {
    position: absolute; right: 20px; top: 232px;
    font-size: 33px; color: var(--ghost-grey);
  }
</style>
</head>
<body>
<main class="stage">
  <section class="card card-front" aria-label="Business card front">
    <div class="brand-mark">
      <div class="figure-area" role="img" aria-label="Illustration of an elegant woman in a red evening dress"></div>
    </div>
    <div class="brand-name">Valdet</div>
    <div class="brand-tagline">Apparel and Accessories</div>
    <div class="person-name">Employee Name</div>
    <div class="person-title">Managing Director</div>
    <div class="contact">
      <div class="phone-row">
        <svg class="phone-icon" viewBox="0 0 18 18" aria-hidden="true">
          <rect width="18" height="18" rx="2" fill="var(--brand-red)"/>
          <path d="M4 6.5c0-1.2 2.2-2 5-2s5 .8 5 2v1h-2.4V6.4H6.4v1.1H4z" fill="#fff"/>
          <rect x="5" y="8.5" width="8" height="5" rx="1" fill="#fff"/>
          <circle cx="9" cy="11" r="1.3" fill="var(--brand-red)"/>
        </svg>
        <span>424-639-8852</span>
      </div>
      <div class="address">3847 North Pelham St.<br>Los Angeles California</div>
    </div>
  </section>

  <section class="card card-back" aria-label="Business card back">
    <div class="ghost-name">Valdet</div>
    <div class="ghost-tagline">Apparel and Accessories</div>
  </section>
</main>
</body>
</html>
```